Fitness business need 3x3 card to promote 6wk boot camp nutrition challenge

Hi, we're looking for someone to make our current card look better and more modern. We want to keep the text the same, but we want a better design. We also want to keep the woman on the front of the card. The card is for both men and women so we want it to feel inclusive and bright. The idea is to make the card look more modern. We want some pops of color. The main feature is to promote the pricing on the back of the card. It would be nice if that continues to look like a coupon or if it stands out with a bright color or background.

Target Market(s)

Men and women looking to get in shape

Industry/Entity Type

Fitness

Font styles to use
Serif
Sans Serif

Colors
3176b5
0255a3
33a6d7
f37122
ec1f27

Requirements
Must have
• front and back, use pic of women provided

```html
<!DOCTYPE html>
<html lang="en">
<head>
<meta charset="utf-8">
<title>Boot Camp Card – Back</title>
<link rel="stylesheet" href="https://fonts.googleapis.com/css2?family=Montserrat:wght@600;700&family=Quicksand:wght@300;400;700&display=swap">
<style>
  :root {
    --bg-orange: #e06a45;
    --bg-mauve: #a27d8a;
    --bg-blue: #3a73b4;
    --band-orange: #f05a2c;
    --band-red: #d83c3c;
    --ink: #ffffff;
  }
  html, body {
    margin: 0;
    padding: 0;
    width: 1200px;
    height: 1200px;
    overflow: hidden;
    background: #ffffff;
  }
  .card { display: block; width: 1200px; height: 1200px; }
  .card text { fill: var(--ink); }
  .title { font-family: "Montserrat", sans-serif; font-weight: 700; font-size: 111px; letter-spacing: -4px; }
  .subtitle { font-family: "Quicksand", sans-serif; font-weight: 400; font-size: 44px; }
  .no-word { font-family: "Quicksand", sans-serif; font-weight: 300; font-size: 80px; }
  .no-item { font-family: "Montserrat", sans-serif; font-weight: 700; font-size: 33px; }
  .no-item-small { font-family: "Montserrat", sans-serif; font-weight: 700; font-size: 25px; }
  .bang { font-family: "Quicksand", sans-serif; font-weight: 300; font-size: 62px; }
  .pitch { font-family: "Quicksand", sans-serif; font-weight: 400; font-size: 40px; }
  .pitch .strong { font-family: "Montserrat", sans-serif; font-weight: 700; }
  .big-six { font-family: "Quicksand", sans-serif; font-weight: 300; font-size: 212px; }
  .weeks { font-family: "Quicksand", sans-serif; font-weight: 300; font-size: 94px; letter-spacing: -2px; }
  .for-only { font-family: "Montserrat", sans-serif; font-weight: 700; font-size: 62px; letter-spacing: -2px; }
  .price { font-family: "Montserrat", sans-serif; font-weight: 700; font-size: 232px; letter-spacing: -6px; }
  .contact-light { font-family: "Quicksand", sans-serif; font-weight: 400; }
  .contact-bold { font-family: "Montserrat", sans-serif; font-weight: 600; }
  .logo-name { font-family: "Quicksand", sans-serif; font-weight: 700; font-size: 24px; }
  .rule { stroke: var(--ink); stroke-width: 3; }
  .logo-ring { fill: none; stroke: var(--ink); stroke-width: 3; }
</style>
</head>
<body>
<svg class="card" viewBox="0 0 1200 1200" xmlns="http://www.w3.org/2000/svg" aria-label="Boot camp card back">
  <defs>
    <linearGradient id="bg-fade" x1="0" y1="0" x2="1" y2="0">
      <stop offset="0" stop-color="var(--bg-orange)"/>
      <stop offset="0.5" stop-color="var(--bg-mauve)"/>
      <stop offset="1" stop-color="var(--bg-blue)"/>
    </linearGradient>
    <linearGradient id="band-fade" x1="0" y1="0" x2="1" y2="0">
      <stop offset="0" stop-color="var(--band-orange)"/>
      <stop offset="1" stop-color="var(--band-red)"/>
    </linearGradient>
  </defs>

  <rect class="background" width="1200" height="1200" fill="url(#bg-fade)"/>
  <polygon class="price-band" points="0,735 1200,465 1200,919 0,919" fill="url(#band-fade)"/>

  <!-- heading -->
  <text class="title" x="178" y="131">Boot CAMP Title</text>
  <text class="subtitle" x="178" y="183">6 Week Fitness &amp; Nutrition Boot Camp</text>
  <line class="rule" x1="178" y1="206" x2="1034" y2="206"/>

  <!-- no barbells / no heavy weights -->
  <text class="no-word" x="272" y="290">NO</text>
  <text class="no-item" x="393" y="277">BARBELLS</text>
  <text class="bang" x="588" y="290">!</text>
  <text class="no-word" x="673" y="290">NO</text>
  <text class="no-item" x="797" y="257">HEAVY</text>
  <text class="no-item-small" x="797" y="290">WEIGHTS</text>
  <text class="bang" x="918" y="290">!</text>
  <line class="rule" x1="178" y1="326" x2="1034" y2="326"/>

  <!-- pitch -->
  <text class="pitch" x="211" y="385"><tspan class="strong">Burn fat,</tspan> build muscle &amp; have fun! Tons</text>
  <text class="pitch" x="211" y="438">of classes led by world-class coaches.</text>
  <text class="pitch" x="211" y="491">Personalized nutrition planning, prizes,</text>
  <text class="pitch" x="211" y="545">and more! <tspan class="strong">Sign up Today!</tspan></text>

  <!-- price offer -->
  <text class="big-six" x="100" y="865">6</text>
  <text class="weeks" x="217" y="796">WEEKS</text>
  <text class="for-only" x="217" y="857">FOR ONLY</text>
  <text class="price" x="588" y="837">$249</text>

  <!-- contact -->
  <g text-anchor="middle">
    <text class="contact-light" x="600" y="968" font-size="31">Learn More at</text>
    <text class="contact-bold" x="600" y="1021" font-size="31">www.YourGymURL.com/landingpage</text>
    <text class="contact-light" x="600" y="1073" font-size="40">(555) 555-5555</text>
    <text class="contact-bold" x="600" y="1120" font-size="37">17 Street Name</text>
    <text class="contact-light" x="600" y="1169" font-size="40">City Name, State 10003</text>
  </g>

  <!-- logo placeholders -->
  <g class="logo logo-left" text-anchor="middle">
    <circle class="logo-ring" cx="149" cy="1062" r="73"/>
    <text class="logo-name" x="149" y="1058">YOUR</text>
    <text class="logo-name" x="149" y="1084">LOGO</text>
  </g>
  <g class="logo logo-right" text-anchor="middle">
    <circle class="logo-ring" cx="1053" cy="1047" r="73"/>
    <text class="logo-name" x="1053" y="1043">YOUR</text>
    <text class="logo-name" x="1053" y="1069">LOGO</text>
  </g>
</svg>
</body>
</html>
```